Korvell Plant Services

We are a heavy diesel mechanical business with additional air con certificates, remapping engine rebuilt

Contact Information for Business Card

Company Name, Director Name, Managing Director, Contact details, email and website

Font styles to use
Serif
Script

```html
<!DOCTYPE html>
<html lang="en">
<head>
<meta charset="UTF-8">
<title>Korvell Plant Services – Business Card</title>
<link href="https://fonts.googleapis.com/css2?family=Great+Vibes&family=Playfair+Display:wght@400;700&display=swap" rel="stylesheet">
<style>
  :root{
    --backdrop:#8f8f8f;
    --navy:#2f3d7a;
    --white:#ffffff;
    --photo-light:#d8cdcf;
    --photo-warm:#b89a8c;
  }
  *{box-sizing:border-box;margin:0;padding:0}
  html,body{width:1200px;height:1200px;overflow:hidden}
  body{background:var(--backdrop);font-family:"Playfair Display",serif;color:var(--white);position:relative}

  .card{position:absolute;left:227px;width:746px;height:435px;border-radius:24px;overflow:hidden;background:var(--navy)}
  .card--front{top:127px}
  .card--back{top:614px}

  .brand{position:absolute;text-align:center;font-family:"Playfair Display",serif;font-weight:700;line-height:1}
  .brand .brand-main,.brand .brand-sub{display:block}

  .front-brand{left:560px;top:306px;width:120px}
  .front-brand .brand-main{font-size:28px}
  .front-brand .brand-sub{font-size:12px;margin-top:3px}

  .site-photo{position:absolute;left:0;top:0;width:100%;height:210px;
    background:linear-gradient(180deg,var(--photo-light) 0%,var(--photo-warm) 100%)}

  .details{position:absolute;left:48px;top:252px}
  .person-name{font-weight:700;font-size:19px;letter-spacing:.3px;line-height:1.3}
  .person-role{font-family:"Great Vibes",cursive;font-size:26px;line-height:1.1}
  .contact-list{list-style:none;margin-top:18px}
  .contact-list li{display:flex;align-items:center;gap:10px;font-size:18px;line-height:25px}
  .contact-list svg{width:16px;height:16px;flex:none}

  .back-brand{left:460px;top:262px;width:250px}
  .back-brand .brand-main{font-size:58px}
  .back-brand .brand-sub{font-size:21px;margin-top:8px}
</style>
</head>
<body>

<section class="card card--front">
  <div class="brand front-brand">
    <span class="brand-main">Korvell</span>
    <span class="brand-sub">Plant Services</span>
  </div>
</section>

<section class="card card--back">
  <div class="site-photo" role="img" aria-label="Photo of a tracked tractor and an excavator on a low-loader trailer at a work site"></div>

  <div class="details">
    <p class="person-name">DIRECTOR NAME</p>
    <p class="person-role">Managing Director</p>
    <ul class="contact-list">
      <li>
        <svg viewBox="0 0 24 24" aria-hidden="true"><path fill="var(--white)" d="M6.6 10.8a15.5 15.5 0 0 0 6.6 6.6l2.2-2.2a1 1 0 0 1 1-.25 11.4 11.4 0 0 0 3.6.6 1 1 0 0 1 1 1V20a1 1 0 0 1-1 1A17 17 0 0 1 3 4a1 1 0 0 1 1-1h3.5a1 1 0 0 1 1 1 11.4 11.4 0 0 0 .6 3.6 1 1 0 0 1-.25 1z"/></svg>
        <span>0400 123 987</span>
      </li>
      <li>
        <svg viewBox="0 0 24 24" aria-hidden="true"><rect x="2.5" y="5" width="19" height="14" rx="1.5" fill="none" stroke="var(--white)" stroke-width="1.6"/><path d="M3 6l9 7 9-7" fill="none" stroke="var(--white)" stroke-width="1.6"/></svg>
        <span>admin@korvellplant.net</span>
      </li>
      <li>
        <svg viewBox="0 0 24 24" aria-hidden="true"><g fill="none" stroke="var(--white)" stroke-width="1.6"><circle cx="12" cy="12" r="9.5"/><ellipse cx="12" cy="12" rx="4.2" ry="9.5"/><path d="M2.5 12h19"/></g></svg>
        <span>korvellplant.net</span>
      </li>
    </ul>
  </div>

  <div class="brand back-brand">
    <span class="brand-main">Korvell</span>
    <span class="brand-sub">Plant Services</span>
  </div>
</section>

</body>
</html>
```